Letter and Envelope Design For Larchmont Realty

Please design a letter and an envelope incorporating our logo (See Attached). We are also launched a business card contest. Since we want them to match, please feel free to submit a design for both the business card and also the letter design and envelope.

Requirements
Must have
• The envelope, the letter and the business cards must match somehow connecting the designs. We want them to have something that holds them together besides the logo.

```html
<!DOCTYPE html>
<html lang="en">
<head>
<meta charset="utf-8">
<title>Larchmont Realty Stationery</title>
<link href="https://fonts.googleapis.com/css2?family=Montserrat:wght@500&family=Work+Sans:wght@400;500&display=swap" rel="stylesheet">
<style>
:root{
  --navy:#27307f;
  --ink:#555a66;
  --dark:#333640;
  --paper:#ffffff;
  --backdrop:#ebebeb;
  --shadow:0 2px 6px rgba(0,0,0,.18);
}
*{box-sizing:border-box;margin:0;padding:0}
html,body{width:1200px;height:762px;overflow:hidden}
body{background:var(--backdrop);font-family:"Work Sans",sans-serif;color:var(--ink);position:relative}
.sheet{position:absolute;background:var(--paper);box-shadow:var(--shadow)}
.brand-name{font-family:"Montserrat",sans-serif;font-weight:500;color:var(--navy);text-transform:uppercase;letter-spacing:.14em;white-space:nowrap}
.brand-ring{border:2px solid var(--navy);border-radius:50%}
.icon{width:7px;height:7px;vertical-align:-1px;margin-right:3px}

/* Letterhead */
.letter{left:45px;top:52px;width:466px;height:658px}
.letter .brand{position:absolute;left:34px;top:28px;display:flex;flex-direction:column;align-items:center;width:90px}
.letter .brand-ring{width:34px;height:34px}
.letter .brand-name{font-size:8px;margin-top:6px;text-align:center;line-height:1.3}
.letter .divider{position:absolute;left:224px;top:30px;width:1px;height:53px;background:var(--navy)}
.letter .contact{position:absolute;left:332px;top:28px;font-size:7.5px;line-height:10.6px;color:var(--ink)}
.letter .contact .gap{height:4px}
.contact strong{color:var(--navy);font-weight:500}
.letter .salutation{position:absolute;left:34px;top:174px;font-size:13.5px;color:var(--navy)}
.letter .body{position:absolute;left:34px;top:208px;width:400px;font-size:9.1px;line-height:12px;color:var(--ink)}
.letter .body p{margin-bottom:15px}
.letter .closing{position:absolute;left:34px;top:496px;font-size:10px;color:var(--dark)}
.letter .signature{display:block;width:84px;height:16px;margin:6px 0 9px;background:linear-gradient(90deg,rgba(51,54,64,.18),rgba(51,54,64,.05));border-radius:8px}
.letter .signer{font-size:9.6px;color:var(--dark)}
.letter .role{font-size:7.4px;color:var(--dark);margin-top:1px}
.letter .company{font-size:6px;color:var(--dark);margin-top:3px;text-transform:uppercase;letter-spacing:-.01em}

/* Compliment card */
.card{left:549px;top:52px;width:605px;height:302px}
.card .brand{position:absolute;left:23px;top:22px;display:flex;flex-direction:column;align-items:center;width:140px}
.card .brand-ring{width:55px;height:55px}
.card .brand-name{font-size:12px;margin-top:9px;text-align:center;line-height:1.3}
.card .rule{position:absolute;left:24px;top:232px;width:267px;height:1px;background:var(--navy)}
.card .contact{position:absolute;left:24px;top:245px;font-size:10px;line-height:13.6px;color:var(--dark);letter-spacing:.02em}
.card .address{position:absolute;left:184px;top:258.6px;font-size:10px;line-height:13.6px;color:var(--dark);letter-spacing:.02em}

/* Envelope */
.envelope{left:549px;top:408px;width:605px;height:302px;background:var(--navy);overflow:hidden}
.envelope .flap{position:absolute;left:0;top:0}
.envelope .flap-mark{position:absolute;left:275px;top:19px;width:55px;height:55px;border:2px solid rgba(255,255,255,.08);border-radius:50%}
.envelope .brand{position:absolute;left:0;top:152px;width:605px;display:flex;flex-direction:column;align-items:center}
.envelope .brand-ring{width:62px;height:62px;border:3px solid #fff}
.envelope .brand-name{color:#fff;font-size:15px;margin-top:12px;text-align:center;line-height:1.35}
</style>
</head>
<body>

<section class="sheet letter" aria-label="Letterhead">
  <div class="brand">
    <span class="brand-ring"></span>
    <span class="brand-name">Larchmont<br>Realty</span>
  </div>
  <span class="divider"></span>
  <div class="contact">
    48 Harlow Lane,<br>Ashford, NZ, 7022
    <div class="gap"></div>
    <svg class="icon" viewBox="0 0 10 10"><path d="M2 1l2 1-1 2c1 2 2 3 3 3l1-1 2 2-1 1C4 9 1 6 1 2z" fill="var(--navy)"/></svg>(514) 555-0172<br>
    <svg class="icon" viewBox="0 0 10 10"><rect x="1" y="2" width="8" height="6" fill="none" stroke="var(--navy)"/><path d="M1 2l4 3 4-3" fill="none" stroke="var(--navy)"/></svg>hello@larchmontrealty.com<br>
    <svg class="icon" viewBox="0 0 10 10"><circle cx="5" cy="5" r="4" fill="var(--navy)"/></svg>www.<strong>larchmontrealty</strong>.com
  </div>
  <h2 class="salutation" style="font-weight:400">Dear Sir</h2>
  <div class="body">
    <p>Lorem ipsum dolor sit amet, an vel recteque dissentiet, detracto albucius platonem ex vel, eros repudiandae cu. Atqui aliquando nec an, unum graece adolescens vel ad. Id odio scae has, iudico euismod atomorum ius ea, cum ea honestatis quaerendum theophrastus. Mea honestatis quaerendum theophrastus. Mea</p>
    <p>Lorem ipsum dolor sit amet, an vel recteque dissentiet, detracto albucius platonem ex vel, eros repudiandae cu. Atqui aliquando nec an, unum graece adolescens vel ad. Id odio scae has, iudico euismod atomorum ius ea, cum ea honestatis quaerendum theophrastus. Mea doming repudiandae ex, cu cum civibus assentior posidonium. Quo etiam pertinax ex, te eros repudiandae cu. Atqui aliquando nec an, unum graece adolescens vel ad. Id odio scae honestatis quaerendum theophrastus. Mea</p>
    <p>Lorem ipsum dolor sit amet, an vel recteque dissentiet, detracto albucius platonem ex vel, eros repudiandae cu. Atqui aliquando nec an, unum graece adolescens vel ad. Id odio scae has, iudico euismod atomorum ius ea, cum ea honestatis quaerendum theophrastus. Mea honestatis quaerendum theophrastus. Mea</p>
    <p>Lorem ipsum dolor sit amet, an vel recteque dissentiet, detracto albucius platonem ex vel, eros repudiandae cu. Atqui aliquando nec an, unum graece adolescens vel ad. Id odio scae has, iudico euismod atomorum ius ea, cum ea honestatis quaerendum theophrastus. Mea honestatis quaerendum theophrastus. Mea</p>
  </div>
  <div class="closing">
    Kind Regards
    <span class="signature" role="img" aria-label="Handwritten signature of Daniel Whitford"></span>
    <div class="signer">Daniel Whitford</div>
    <div class="role">Chief Alchemist</div>
    <div class="company">Harbourline Property Group Ltd</div>
  </div>
</section>

<section class="sheet card" aria-label="Compliment card">
  <div class="brand">
    <span class="brand-ring" style="border-width:3px"></span>
    <span class="brand-name">Larchmont<br>Realty</span>
  </div>
  <span class="rule"></span>
  <div class="contact">
    <svg class="icon" viewBox="0 0 10 10"><path d="M2 1l2 1-1 2c1 2 2 3 3 3l1-1 2 2-1 1C4 9 1 6 1 2z" fill="var(--navy)"/></svg>(514) 555-0172<br>
    <svg class="icon" viewBox="0 0 10 10"><rect x="1" y="2" width="8" height="6" fill="none" stroke="var(--navy)"/><path d="M1 2l4 3 4-3" fill="none" stroke="var(--navy)"/></svg>hello@larchmontrealty.com<br>
    <svg class="icon" viewBox="0 0 10 10"><circle cx="5" cy="5" r="4" fill="var(--navy)"/></svg>www.<strong>larchmontrealty</strong>.com
  </div>
  <div class="address">48 Harlow Lane,<br>Ashford, NZ, 7022</div>
</section>

<section class="sheet envelope" aria-label="Envelope">
  <svg class="flap" width="605" height="100" viewBox="0 0 605 100">
    <path d="M10 0 C12 50 14 94 60 94 L545 94 C591 94 593 50 595 0" fill="none" stroke="rgba(0,0,0,.28)" stroke-width="2"/>
  </svg>
  <span class="flap-mark"></span>
  <div class="brand">
    <span class="brand-ring"></span>
    <span class="brand-name">Larchmont<br>Realty</span>
  </div>
</section>

</body>
</html>
```